Health care technology software systems

We have a solid logo. We have company colors that will need to be used as well. We just need a great business card design. We sell to health plans but want to be modern
Updates

Need extra days to review

Target Market(s)

Health technology sector selling into Health Plans

Industry/Entity Type

Health Care Technology

Contact Information for Business Card

Name, title, address, phone number, email

Requirements
Must have
• Use of Kembrata corporate colors - Uploaded w/ our logos

```html
<!DOCTYPE html>
<html lang="en">
<head>
<meta charset="utf-8">
<title>Kembrata Business Card</title>
<link rel="stylesheet" href="https://fonts.googleapis.com/css2?family=Source+Sans+3:wght@400;700&display=swap">
<style>
  :root {
    --stage: #1f2223;
    --paper: #ffffff;
    --brand-sky: #47cdfd;
    --brand-sky-soft: #6fd8fd;
    --ink: #23272a;
    --type: #ffffff;
  }
  html, body {
    margin: 0;
    padding: 0;
    width: 927px;
    height: 1200px;
    overflow: hidden;
    background: var(--stage);
  }
  .stage {
    position: relative;
    width: 927px;
    height: 1200px;
  }
  .card {
    position: absolute;
    left: 80px;
    width: 768px;
    height: 438px;
    display: block;
  }
  .card--front { top: 162px; }
  .card--back { top: 657px; height: 439px; }
  .paper { fill: var(--paper); }
  .band { fill: var(--brand-sky); }
  .brand-dot { fill: var(--brand-sky); }
  .brand-name {
    font-family: "Source Sans 3", sans-serif;
    font-weight: 400;
    fill: var(--ink);
  }
  .holder-name {
    font-family: "Source Sans 3", sans-serif;
    font-weight: 700;
    font-size: 84px;
    fill: var(--type);
  }
  .holder-title, .contact-line {
    font-family: "Source Sans 3", sans-serif;
    font-weight: 400;
    fill: var(--type);
  }
  .holder-title { font-size: 56px; }
  .contact-line { font-size: 46px; }
  .contact-icon {
    fill: none;
    stroke: var(--type);
    stroke-width: 2.5;
    stroke-linejoin: round;
  }
</style>
</head>
<body>
<main class="stage">
  <svg class="card card--front" viewBox="0 0 1399 797" aria-label="Business card front">
    <defs>
      <linearGradient id="edge-soft" x1="0" y1="0" x2="1" y2="0">
        <stop offset="0" stop-color="#6fd8fd"/>
        <stop offset="1" stop-color="#47cdfd"/>
      </linearGradient>
    </defs>
    <rect class="paper" width="1399" height="797"/>
    <rect class="band" x="743" y="0" width="656" height="797"/>
    <rect class="edge-pattern" x="657" y="0" width="86" height="797" fill="url(#edge-soft)"
          role="img" aria-label="Column of blue diamond tiles along the panel edge"/>

    <g class="brand">
      <circle class="brand-dot" cx="349" cy="355" r="40"/>
      <text class="brand-name" x="349" y="545" font-size="82" text-anchor="middle">Kembrata</text>
    </g>

    <g class="holder">
      <text class="holder-name" x="788" y="168">Owen Marlow</text>
      <text class="holder-title" x="790" y="216">Director General</text>
    </g>

    <g class="address">
      <text class="contact-line" x="790" y="480">2417 Harlow Lane</text>
      <text class="contact-line" x="788" y="533">Pine Ridge, LA 71352</text>
    </g>

    <g class="contact">
      <g class="contact-icon">
        <rect x="797" y="588" width="20" height="36" rx="3"/>
        <rect x="801" y="596" width="12" height="14"/>
        <circle cx="807" cy="618" r="2"/>
      </g>
      <text class="contact-line" x="848" y="623">+1 xxx yyy xxxx</text>
      <g class="contact-icon">
        <polygon points="791,668 823,654 813,680 805,671"/>
        <line x1="805" y1="671" x2="823" y2="654"/>
      </g>
      <text class="contact-line" x="848" y="680">hello@kembrata.com</text>
    </g>
  </svg>

  <svg class="card card--back" viewBox="0 0 1399 799" aria-label="Business card back">
    <defs>
      <linearGradient id="top-soft" x1="0" y1="0" x2="0" y2="1">
        <stop offset="0" stop-color="#47cdfd"/>
        <stop offset="1" stop-color="#6fd8fd"/>
      </linearGradient>
      <linearGradient id="bottom-soft" x1="0" y1="1" x2="0" y2="0">
        <stop offset="0" stop-color="#47cdfd"/>
        <stop offset="1" stop-color="#6fd8fd"/>
      </linearGradient>
    </defs>
    <rect class="paper" width="1399" height="799"/>

    <rect class="band" x="0" y="0" width="1399" height="110"/>
    <rect class="edge-pattern" x="0" y="110" width="1399" height="44" fill="url(#top-soft)"
          role="img" aria-label="Row of blue diamond tiles along the top band"/>

    <rect class="edge-pattern" x="0" y="647" width="1399" height="44" fill="url(#bottom-soft)"
          role="img" aria-label="Row of blue diamond tiles along the bottom band"/>
    <rect class="band" x="0" y="691" width="1399" height="108"/>

    <g class="brand">
      <circle class="brand-dot" cx="699" cy="356" r="40"/>
      <text class="brand-name" x="699" y="548" font-size="82" text-anchor="middle">Kembrata</text>
    </g>
  </svg>
</main>
</body>
</html>
```